Need modern simple design for magazine ad, apartment and condo roofer.

I need a half page magazine ad for a local roofer to publish in an industry magazine. Apartment associations industry. All types of roofs. Shingle and Flat
Need the design to be creative and modern, clean and simple. I do not want a busy design. One that stands out and makes a point quickly.
Logo must be prominent.
DO NOT USE PHOTOS FROM MY WEBSITE PLEASE. Looking for something new.
I work on entire complexes not houses.

Need to make sure our phone number and email address are listed at the bottom. Here is my website www.pelvornroofs.com
Want to stay away from standard clip arts of tools, homes, apartment buildings.
Half Horizontal 7.25 x 4.75
Ads should be in PDF and JPG format.

Target Market(s)

Apartment or Condo owners looking for large scale roofing projects

Industry/Entity Type

Roofing

Requirements
Must have
• Prominent Logo
Simple Clean Design
Create graphics
Not Busy
Should not have
• Clip Art
No Photos from my website

```html
<!DOCTYPE html>
<html lang="en">
<head>
<meta charset="utf-8">
<title>Pelvorn Roofing – Half Page Ad</title>
<link href="https://fonts.googleapis.com/css2?family=Playfair+Display:wght@700&family=Roboto+Condensed:wght@700&display=swap" rel="stylesheet">
<style>
  :root {
    --blue-top: #2c6db0;
    --blue-bottom: #21548b;
    --brand-blue: #2a63a3;
    --band-grey: #bcbfc3;
    --white: #ffffff;
    --roof-light: #8a8689;
    --roof-dark: #4a4547;
  }
  html, body {
    margin: 0;
    padding: 0;
    width: 1200px;
    height: 867px;
    overflow: hidden;
    background: var(--white);
  }
  .ad {
    position: relative;
    width: 1200px;
    height: 867px;
    overflow: hidden;
    background: var(--white);
    font-family: "Roboto Condensed", "Arial Narrow", sans-serif;
  }
  .header-area {
    position: absolute;
    left: 0; top: 0;
    width: 1200px; height: 292px;
    background: var(--white);
  }
  .roof-photo {
    position: absolute;
    left: 0; top: 292px;
    width: 1200px; height: 575px;
    background: linear-gradient(160deg, var(--roof-light) 0%, #6b6668 45%, var(--roof-dark) 100%);
  }
  .brand {
    position: absolute;
    left: 50px; top: 100px;
    display: flex;
    align-items: center;
    gap: 16px;
  }
  .brand-mark {
    width: 64px; height: 64px;
    background: var(--brand-blue);
  }
  .brand-name {
    font-size: 58px;
    font-weight: 700;
    color: var(--brand-blue);
    line-height: 1;
    white-space: nowrap;
  }
  .banner {
    position: absolute;
    left: 0; top: 0;
  }
  .headline {
    position: absolute;
    left: 499px; width: 634px;
    top: 0;
    text-align: center;
    font-family: "Playfair Display", Georgia, serif;
    font-weight: 700;
    color: var(--white);
  }
  .headline span {
    position: absolute;
    left: 0; right: 0;
    line-height: 1;
  }
  .headline .line-1 { top: 108px; font-size: 86px; }
  .headline .line-2 { top: 196px; font-size: 70px; }
  .headline .line-3 { top: 262px; font-size: 86px; }
  .services {
    position: absolute;
    left: 509px; width: 634px;
    top: 386px; height: 73px;
    background: var(--band-grey);
    color: var(--brand-blue);
    font-size: 38px;
    font-weight: 700;
    display: flex;
    align-items: center;
    justify-content: center;
    white-space: nowrap;
  }
  .contact {
    position: absolute;
    left: 499px; width: 634px;
    color: var(--white);
    font-weight: 700;
    display: flex;
    align-items: center;
    justify-content: center;
    gap: 14px;
    white-space: nowrap;
  }
  .contact-phone { top: 484px; font-size: 64px; }
  .contact-email { top: 566px; font-size: 41px; }
</style>
</head>
<body>
<div class="ad">
  <div class="header-area"></div>
  <div class="roof-photo" role="img" aria-label="Close-up photograph of dark grey clay roof tiles in rows"></div>

  <div class="brand">
    <div class="brand-mark"></div>
    <div class="brand-name">Pelvorn Roofing</div>
  </div>

  <svg class="banner" width="1200" height="867" viewBox="0 0 1200 867" aria-hidden="true">
    <defs>
      <linearGradient id="bannerFill" x1="0" y1="0" x2="0" y2="1">
        <stop offset="0" stop-color="var(--blue-top)"/>
        <stop offset="1" stop-color="var(--blue-bottom)"/>
      </linearGradient>
    </defs>
    <polygon points="499,0 1133,0 1133,570 816,759 499,570" fill="url(#bannerFill)"/>
  </svg>

  <div class="headline">
    <span class="line-1">APARTMENT</span>
    <span class="line-2">ASSOCIATIONS</span>
    <span class="line-3">INDUSTRY</span>
  </div>

  <div class="services">All types of roofs. Shingle And Flat</div>

  <div class="contact contact-phone">
    <svg width="26" height="46" viewBox="0 0 26 46" aria-hidden="true">
      <rect x="2" y="2" width="22" height="42" rx="4" fill="none" stroke="#fff" stroke-width="3"/>
      <line x1="2" y1="9" x2="24" y2="9" stroke="#fff" stroke-width="2"/>
      <line x1="2" y1="35" x2="24" y2="35" stroke="#fff" stroke-width="2"/>
      <circle cx="13" cy="40" r="2" fill="#fff"/>
    </svg>
    <span>555.014.2270</span>
  </div>

  <div class="contact contact-email">
    <svg width="40" height="26" viewBox="0 0 40 26" aria-hidden="true">
      <rect x="1.5" y="1.5" width="37" height="23" fill="none" stroke="#fff" stroke-width="2.5"/>
      <polyline points="1.5,1.5 20,15 38.5,1.5" fill="none" stroke="#fff" stroke-width="2.5"/>
      <line x1="1.5" y1="24.5" x2="15" y2="11" stroke="#fff" stroke-width="2"/>
      <line x1="38.5" y1="24.5" x2="25" y2="11" stroke="#fff" stroke-width="2"/>
    </svg>
    <span>info@pelvornroofs.com</span>
  </div>
</div>
</body>
</html>
```